Brochure design for International Beauty Trade Show

I neee a tri-fold company products' brochure to distribute to customers at an international trade show coming soon. We have 4 main product categories- hair and skincare, facial care, Body and bath and massage oil.
The brochure needs to include at least 2 photos of the main products of each category, benefits, call to action and our company contact info ( website and phone number).

Target Market(s)

Educated and high income earners looking for all-natural,pure, 100 organic products for their beauty and personal care needs. Our products cross all racial groups/demographics and suitable for all skin types

Industry/Entity Type

Hair And Beauty

Font styles to use
Serif

Colors

Designer to choose colors to be used in the design.

Requirements
Must have
• The design must stand out as pure and luxury and at the same time be inclusive using our logo design colors- orange and blue. Also, the content must be easy to read and captivating.
• Finally if using women pictures, please include Black, white, Asian and Latina to reflect the fact that our products are suitable for all skin types.
Nice to have
• Design the brochure such that it could be printed as a poster-banner ad.
Should not have
• Cookie cutter designs are not welcome

```html
<!DOCTYPE html>
<html lang="en">
<head>
<meta charset="utf-8">
<title>Veloria Naturals – Tri-fold Brochure</title>
<link href="https://fonts.googleapis.com/css2?family=Ubuntu:wght@400;500;700&family=Open+Sans:wght@400;600&display=swap" rel="stylesheet">
<style>
:root{
  --blue:#1a8fd1;
  --blue-deep:#0f74b5;
  --orange:#ee6d1c;
  --ink:#2e2e33;
  --paper:#f7f8fa;
  --peach:#fbd9bd;
  --sky:#cfe7f7;
  --stage:#e9eaec;
}
*{box-sizing:border-box;margin:0;padding:0}
html,body{width:1200px;height:900px;overflow:hidden;background:var(--stage)}
body{position:relative;font-family:"Open Sans",Arial,sans-serif;color:var(--ink)}
.sheet{position:absolute;left:30px;width:1140px;height:420px;display:flex;
  background:linear-gradient(120deg,var(--peach) 0%,var(--paper) 35%,var(--paper) 65%,var(--sky) 100%);
  box-shadow:0 6px 18px rgba(0,0,0,.15);overflow:hidden}
.sheet--outside{top:20px}
.sheet--inside{top:460px}
.panel{position:relative;width:380px;height:100%;border-right:1px solid rgba(0,0,0,.06)}
.panel:last-child{border-right:none}
.photo{position:absolute;display:block}
.band{position:absolute;left:0;right:0;height:36px;color:#fff;font-family:"Ubuntu",sans-serif;
  font-weight:500;font-size:22px;line-height:36px;padding-left:24px}
.band--blue{background:var(--blue)}
.band--orange{background:var(--orange);text-align:center;padding-left:0}
.benefits{position:absolute;left:24px;right:20px;list-style:none;font-size:12.5px;line-height:21px}
.benefits li::before{content:"";display:inline-block;width:7px;height:7px;border-radius:50%;
  border:1.5px solid var(--ink);margin-right:9px;vertical-align:1px}
/* outside */
.about{position:absolute;left:0;top:0;width:380px;height:150px;background:var(--blue);color:#fff;padding:18px 24px}
.about__title{font-family:"Ubuntu",sans-serif;font-weight:500;font-size:24px;border-bottom:2px solid #fff;display:inline-block;padding-bottom:2px;margin-bottom:10px}
.about__text{font-size:12px;line-height:17px;text-align:justify}
.portrait{position:absolute;left:130px;top:150px;width:124px;height:124px;border-radius:50%;border:5px solid var(--orange)}
.contact{position:absolute;left:0;right:0;top:290px;text-align:center;font-size:14px;line-height:19px}
.contact__title{font-family:"Ubuntu",sans-serif;font-weight:700;font-size:19px;color:var(--blue)}
.contact__phone{font-size:16px}
.mark{display:inline-flex;align-items:center;gap:7px;font-family:"Ubuntu",sans-serif;font-weight:700;color:var(--orange)}
.mark__dot{border-radius:50%;background:var(--orange)}
.contact .mark{font-size:18px;margin-bottom:4px}
.contact .mark__dot{width:14px;height:14px}
.cover__brand{position:absolute;left:0;right:0;top:275px;text-align:center}
.cover__brand .mark{font-size:30px}
.cover__brand .mark__dot{width:24px;height:24px}
.cover__title{font-family:"Ubuntu",sans-serif;font-size:40px;line-height:40px;margin-top:8px}
.cover__title .t1{color:var(--orange);display:block}
.cover__title .t2{color:var(--blue-deep);display:block}
.cover__tag{font-family:"Ubuntu",sans-serif;font-size:17px;color:var(--blue-deep);margin-top:4px}
</style>
</head>
<body>

<!-- Outside of the brochure -->
<section class="sheet sheet--outside">
  <div class="panel">
    <div class="photo" role="img" aria-label="Photo of argan oil in a glass jar with argan nuts and a white towel on wood"
      style="left:0;top:0;width:380px;height:135px;background:linear-gradient(135deg,#e8e3dc,#8a5a32 55%,#5a351c)"></div>
    <div class="band band--blue" style="top:135px">Hair &amp; Skincare</div>
    <ul class="benefits" style="top:182px">
      <li>Natural moisturizer</li>
      <li>Heal damaged hair or sensitive scalp</li>
      <li>Soften curly and frizzy hair</li>
      <li>Antiaging, remove wrinkles</li>
      <li>Reduce sebum secretion</li>
      <li>Tone, sooth and restore luster</li>
      <li>Restore fair complexion</li>
    </ul>
    <div class="photo" role="img" aria-label="Photo of an oil bottle with seeds and green herbs on a wooden tray"
      style="left:18px;top:338px;width:344px;height:72px;border-radius:6px;background:linear-gradient(90deg,#6b3b1e,#b9892f 50%,#4d6b2a)"></div>
  </div>

  <div class="panel">
    <div class="about">
      <h2 class="about__title">About Us</h2>
      <p class="about__text">Veloria Naturals is an export/import company. Our mission is to satisfy our customers by supplying them with pure, 100% organic products, that make them more attractive and solve the most common skin and hair problems</p>
    </div>
    <svg class="photo" style="left:0;top:140px" width="380" height="60" viewBox="0 0 380 60" aria-hidden="true">
      <path d="M0 10 H380 V18 C300 50 180 0 0 40 Z" fill="var(--blue)"/>
      <path d="M0 40 C180 0 300 50 380 18 V28 C300 60 180 14 0 52 Z" fill="var(--orange)"/>
    </svg>
    <div class="portrait" role="img" aria-label="Round close-up photo of a woman's skin with a magnified detail of dry skin"
      style="background:radial-gradient(circle at 40% 40%,#f1d6c4,#c89c83 70%,#7a5a4b)"></div>
    <div class="contact">
      <div class="mark"><span class="mark__dot"></span>Veloria</div>
      <div class="contact__title">Contact Info:</div>
      <div class="contact__phone">(800) 555-0147</div>
      <div>info@veloria.com</div>
      <div>www.veloria.com</div>
    </div>
  </div>

  <div class="panel">
    <div class="photo" role="img" aria-label="Spa photo of a relaxed woman receiving a facial massage beside a pink lily"
      style="left:0;top:0;width:380px;height:230px;background:linear-gradient(160deg,#c7a487,#f0d4c0 50%,#e6c6b1)"></div>
    <svg class="photo" style="left:0;top:170px" width="380" height="90" viewBox="0 0 380 90" aria-hidden="true">
      <path d="M0 30 C110 80 250 80 380 0 V90 H0 Z" fill="var(--paper)"/>
      <path d="M0 22 C110 70 250 72 380 0 V26 C250 88 110 88 0 42 Z" fill="var(--blue)"/>
      <path d="M0 42 C110 88 250 88 380 26 V32 C250 94 110 94 0 48 Z" fill="var(--orange)"/>
    </svg>
    <div class="cover__brand">
      <div class="mark"><span class="mark__dot"></span>Veloria</div>
      <div class="cover__title"><span class="t1">Natural</span><span class="t2">Solutions</span></div>
      <div class="cover__tag">To Forever Beauty</div>
    </div>
  </div>
</section>

<!-- Inside of the brochure -->
<section class="sheet sheet--inside">
  <div class="panel">
    <div class="photo" role="img" aria-label="Photo of a woman in a towel with a green clay face mask"
      style="left:0;top:0;width:380px;height:125px;background:linear-gradient(120deg,#f3e6d8,#b9b07a 50%,#e9d6c2)"></div>
    <div class="band band--orange" style="top:125px">Facial Care</div>
    <ul class="benefits" style="top:172px">
      <li>Reduce sebum secretion</li>
      <li>Eliminate toxins &amp; blemishes</li>
      <li>Tighten pores</li>
      <li>Dries pimples</li>
      <li>Remove blackheads</li>
    </ul>
    <div class="photo" role="img" aria-label="Photo of prickly pear fruits beside a facial soap package"
      style="left:20px;top:290px;width:340px;height:115px;border-radius:6px;background:linear-gradient(100deg,#e0542a,#f08d3c 35%,#3f7d48 70%,#2b5d8a)"></div>
  </div>

  <div class="panel">
    <div class="band band--blue" style="top:0">Body &amp; Bath Care</div>
    <ul class="benefits" style="top:44px;font-size:12px;line-height:19px">
      <li>Purify and disinfect</li>
      <li>Fight acne</li>
      <li>Rejuvenate &amp; hydrate</li>
      <li>Promote healthy looking skin</li>
      <li>Remove dead cells</li>
    </ul>
    <div class="photo" role="img" aria-label="Photo of a wooden bowl of traditional black soap"
      style="left:40px;top:148px;width:300px;height:140px;border-radius:50%;background:radial-gradient(circle,#6b4a16,#a57b33 60%,#d7b77a)"></div>
    <div class="photo" role="img" aria-label="Photo of lemons beside a lemon soap package"
      style="left:40px;top:300px;width:300px;height:105px;border-radius:6px;background:linear-gradient(90deg,#f5d33a,#f0e27a 40%,#5a9a4e)"></div>
  </div>

  <div class="panel">
    <div class="photo" role="img" aria-label="Photo of massage oil in a glass carafe with black spa stones and green leaves"
      style="left:0;top:0;width:380px;height:125px;background:linear-gradient(120deg,#26342a,#4f6a3a 45%,#c9a53a)"></div>
    <div class="band band--orange" style="top:125px">Massage Care</div>
    <ul class="benefits" style="top:172px">
      <li>Relief stress and pain</li>
      <li>Fight muscle contraction/tenderness</li>
      <li>Eliminate stretch marks</li>
      <li>Pure, undiluted</li>
    </ul>
    <div class="photo" role="img" aria-label="Photo of four amber massage oil pump bottles"
      style="left:60px;top:270px;width:260px;height:135px;border-radius:6px;background:linear-gradient(90deg,#7a3a14,#c0762f 50%,#7a3a14)"></div>
  </div>
</section>

</body>
</html>
```